Book cover for book entitled "Planting Gardens After Winter ....Plus Growing Bright Mornings Within"

I need a book cover for ebook and 6" x 9" paperback print book (print forge pod). I want a simple but "positive" cover with no gothic or darkness in design. I would prefer a "hopeful color scheme" in yellow, blue, green analogous colors and very easy to read main title "Planting Gardens After Winter". I want the tag line of the title. "plus grow bright mornings within" included on the cover please. I am not opposed to white in the color scheme I believe the graphic needs to somehow deal with doors, blocks, keys (perhaps a combination lock since the book is my story of healing from pancreatic cancer through faith, nutrition, and lifestyle changes). I am basically looking for the front cover from you but in a high definition format so it can be transferred to posters and banners for seminar displays. I am uploading my photo in case a designer would want to include a small copy of it in a design although I plan the photo to be on the back cover. The photo could, of course, be cropped.

I would also be interested in seeing a design with a woman  with arms folded and looking satisfied or victorious (happy) casually leaning against a closed door.    It can be very simple....

This graphic could be photo or drawing-even a good line drawing.   Almost whimsical would be okay.  This cover need not be highly complicated but I do want the title easy to read in small or large sizes for ebook and print book.

Reason: I have just changed to "committed" and some new "acceptances" have just come in.

Industry/Entity Type

Nutrition

Font styles to use
Serif

Colors
fbee3e
acd037
33b7a4
34a6d8
3377b5

```html
<!DOCTYPE html>
<html lang="en">
<head>
<meta charset="utf-8">
<title>Planting Gardens After Winter – Book Cover</title>
<link href="https://fonts.googleapis.com/css2?family=Cinzel:wght@400;700&display=swap" rel="stylesheet">
<style>
  :root {
    --page: #ffffff;
    --sun: #fbee3e;
    --leaf: #acd037;
    --teal: #33b7a4;
    --sky: #34a6d8;
    --deep-blue: #3377b5;
    --cream: #fffbe0;
    --spine: #2a5f8f;
  }
  * { margin: 0; padding: 0; box-sizing: border-box; }
  html, body {
    width: 1200px;
    height: 900px;
    overflow: hidden;
    background: var(--page);
  }
  .book-cover {
    position: absolute;
    left: 282px;
    top: 0;
    width: 636px;
    height: 900px;
    overflow: hidden;
    border-left: 12px solid var(--spine);
    background:
      radial-gradient(ellipse 75% 55% at 30% 70%, rgba(251,238,62,0.9) 0%, rgba(251,238,62,0.35) 50%, transparent 78%),
      linear-gradient(165deg, var(--sky) 0%, var(--teal) 38%, var(--leaf) 78%, var(--sun) 100%);
    font-family: 'Cinzel', 'Times New Roman', serif;
  }
  .door-hanger {
    position: absolute;
    left: 36px;
    top: 0;
    width: 486px;
    height: 900px;
    border-radius: 243px 243px 0 0;
    background: linear-gradient(180deg, rgba(255,251,224,0.55) 0%, rgba(255,251,224,0.78) 60%, rgba(255,251,224,0.9) 100%);
  }
  .cover-art {
    position: absolute;
    left: 120px;
    top: 70px;
    width: 420px;
    height: 440px;
    border-radius: 210px 40px 40px 40px;
    background: radial-gradient(circle at 40% 40%, var(--sun) 0%, var(--leaf) 55%, var(--teal) 100%);
    opacity: 0.85;
  }
  .author-band {
    position: absolute;
    left: 522px;
    top: 200px;
    width: 102px;
    height: 700px;
    background: linear-gradient(180deg, rgba(251,238,62,0.5), var(--sun));
  }
  .title {
    position: absolute;
    left: 30px;
    top: 540px;
    width: 500px;
    text-align: center;
    line-height: 1;
    font-weight: 700;
  }
  .title-line { display: block; }
  .title-line--first {
    font-size: 66px;
    color: var(--deep-blue);
  }
  .title-line--middle {
    margin-top: 24px;
    font-size: 46px;
    color: var(--deep-blue);
  }
  .title-line--last {
    margin-top: 26px;
    font-size: 82px;
    color: #1f8a7a;
  }
  .tagline {
    position: absolute;
    left: 30px;
    top: 822px;
    width: 500px;
    text-align: center;
    font-size: 20px;
    font-weight: 400;
    letter-spacing: 0.5px;
    color: var(--deep-blue);
  }
  .author {
    position: absolute;
    left: 562px;
    top: 582px;
    width: 50px;
    text-align: center;
    font-size: 38px;
    line-height: 41px;
    color: var(--deep-blue);
  }
  .author span { display: block; }
</style>
</head>
<body>
  <main class="book-cover">
    <div class="door-hanger"></div>
    <div class="cover-art" role="img" aria-label="Door handle with a hanging sign and awareness ribbon"></div>
    <div class="author-band"></div>

    <h1 class="title">
      <span class="title-line title-line--first">Planting</span>
      <span class="title-line title-line--middle">Gardens After</span>
      <span class="title-line title-line--last">Winter</span>
    </h1>
    <p class="tagline">plus grow bright mornings within</p>

    <p class="author" aria-label="Author">
      <span>A</span><span>U</span><span>T</span><span>H</span><span>O</span><span>R</span>
    </p>
  </main>
</body>
</html>
```